Card Design Project

Gift Card and Gift Card Carrier Design for Spanish Tapas Restaurant/Bar

all of our current logos are on this link:
www.corvo-la-mesa.com/logos.html

you can see the different files, simply click on them to download what you need

the current name of our restaurant is: Corvo-la-mesa's Tapas Bar
we are moving to a new location and we are changing the spelling of our name to:
Valdoreno Tapas Bar

the font that our name is written in is: Mistral

in regards to the tone of the artwork, the look, the feel:
we are Spain Europe Tapas Cuisine.
Our restaurant has two ambiances
one ambiance is a rustic spanish feel on the first floor.
the second ambiance is a trendy ibiza moorish spanish feel.
go to this link for design elements of our new location
http://www.corvo-la-mesa.com/DesignConcepts.html
this is our facebook page:
http://www.facebook.com/corvolamesa

Must provide your actual design files with layers (including all font);
Adobe AI CS4 or lower or
Adobe Photoshop CS4 file or lower

Target Market(s)

ages 25 to 45 is our biggest demographic of customer

Industry/Entity Type

Restaurant

Requirements
Must have
• the front of the gift card is the actual design
the back of the gift card must be the disclaimers for the card

here are the disclaimers:

Additional value may be added to this card at any time.
We are not reponsible for lost, stolen, or damaged cards or any unauthorized card use.
Cards that are lost, stolen, or damaged cannot be replaced and have no value.
Cards cannot be redeemed for cash and cannot be used toward tax and tips.
Card expires 180 calendar days after issue date.

Valdoreno Tapas Bar
2817 West Pellham Street, Chicago IL 60641

i attached samples of the backs of other cards so you can see some samples

Hints to submit a winning design:

In regards to the Logo that we provided you, you will notice the word Valdoreno.
Feel free to not have the word Valdoreno on the front of your gift card inside the logo.
You can remove the layer and only use the logo of the flamenco dancer herself.
If you feel the word Valdoreno goes with your design then keep it.
That logo has become a brand for this restaurant and people know the brand by simply looking at the flamenco lady - so it could be used with the name Valdoreno or without the name Valdoreno.
Feel free to use patterned backgrounds on the front of the card rather than solids
Also, use a different font other than mistral for any other words that you use.
If you use the words Gift Card - use another font for that. If you decide to put the wording: Tapas Bar in your design, or Tapas - use another font, do not use mistral for that wording.

in regards to colors, this restaurant has two ambiances, one is a earthy rustic spanish and another is a loungey darker trendy elegant ambiance, - if you submit really super bright colors all over your card, the super bright features of the card is a bit contradictory to the style of the restaurant.

stay with subtle color shifts and simplicity is the key.

I am going to add a photo of the food delivery bag of the restaurant.
Their food delivery bag is a matte black color bag with a red foil stamp of the flamenco lady logo - it is simple , to the point, and everyone loves the bag when they receive it with their deliveries.

They are also considering to purchase matte black gift cards because they want to do a foil stamped gift card also - so if you use a black background in your design - that can be advantageous to winning the first choice here.

```html
<!DOCTYPE html>
<html lang="en">
<head>
<meta charset="utf-8">
<title>Valdoreno Tapas Bar – Gift Card &amp; Carrier</title>
<link href="https://fonts.googleapis.com/css2?family=Cinzel:wght@500;700&family=Alegreya:wght@400&display=swap" rel="stylesheet">
<style>
  :root{
    --stage-top:#ffffff;
    --stage-bottom:#101010;
    --card-black:#141414;
    --paisley:#e8e4e5;
    --paisley-deep:#ddd7d9;
    --paper:#ffffff;
    --red:#b3111b;
    --dancer-tone:#3a1416;
    --rule:#2a2a2a;
    --strip:#151215;
    --holo:#9a9a9a;
  }
  *{margin:0;padding:0;box-sizing:border-box}
  html,body{width:1200px;height:1000px;overflow:hidden}
  body{
    position:relative;
    background:linear-gradient(180deg,var(--stage-top) 0%,#d9d9d9 30%,#6a6a6a 65%,var(--stage-bottom) 100%);
    font-family:"Alegreya",Georgia,serif;
  }
  .panel{position:absolute}
  .paisley-fill{
    position:absolute;
    background:radial-gradient(circle at 30% 40%,var(--paisley) 0%,var(--paisley-deep) 100%);
  }
  .caps{
    font-family:"Cinzel",Georgia,serif;
    color:var(--red);
    text-align:center;
    position:absolute;left:0;right:0;
    letter-spacing:.28em;
    font-weight:700;
  }
  .dancer{position:absolute;background:var(--dancer-tone);border-radius:6px}

  /* Carrier outside */
  .carrier-front{left:87px;top:19px;width:450px;height:720px;background:var(--card-black)}
  .carrier-front .paisley-fill{left:0;top:0;width:450px;height:124px}
  .carrier-front .enjoy{top:56px;font-size:21px}
  .carrier-address{
    position:absolute;left:0;right:0;top:162px;
    transform:rotate(180deg);
    text-align:center;color:var(--red);
    font-size:13px;line-height:20px;
  }
  .carrier-front .name{top:438px;font-size:18px}
  .carrier-front .dancer{left:175px;top:487px;width:100px;height:140px}
  .carrier-front .giftcard{top:651px;font-size:17px}

  /* Carrier inside */
  .carrier-inside{left:666px;top:19px;width:450px;height:721px;background:var(--paper)}
  .carrier-inside .paisley-fill{left:0;top:0;width:450px;height:598px}
  .field{
    position:absolute;left:49px;right:44px;display:flex;align-items:flex-end;
    font-family:"Cinzel",Georgia,serif;font-weight:700;color:var(--red);
    font-size:22px;letter-spacing:.22em;
  }
  .field .line{flex:1;border-bottom:2px solid var(--rule);margin-left:14px;margin-bottom:6px}
  .field.to{top:66px}
  .field.from{top:140px}
  .field.amount{top:214px}

  /* Card front */
  .card-front{left:140px;top:750px;width:342px;height:222px;background:var(--card-black)}
  .card-front .dancer{left:125px;top:30px;width:95px;height:145px}
  .card-front .url{top:184px;font-size:8.5px;letter-spacing:.3em}

  /* Card back */
  .card-back{left:725px;top:752px;width:341px;height:223px;overflow:hidden}
  .card-back .paisley-fill{inset:0}
  .terms{
    position:absolute;left:0;right:0;top:21px;text-align:center;
    color:var(--red);font-size:8.6px;line-height:12.8px;
  }
  .back-address{
    position:absolute;left:0;right:0;top:104px;text-align:center;
    color:var(--red);font-size:8.6px;line-height:12.8px;
  }
  .holo{position:absolute;left:24px;top:125px;width:70px;height:21px;background:var(--holo)}
  .sig-strip{position:absolute;left:12px;top:165px;width:317px;height:28px;background:var(--strip)}
</style>
</head>
<body>

<section class="panel carrier-front" aria-label="Gift card carrier, outside">
  <div class="paisley-fill" role="img" aria-label="Soft grey paisley pattern band"></div>
  <p class="caps enjoy">Enjoy</p>
  <p class="carrier-address">Valdoreno Tapas Bar<br>2817 West Pellham Street<br>Chicago, IL 60641</p>
  <p class="caps name">Valdoreno Tapas Bar</p>
  <div class="dancer" role="img" aria-label="Red line drawing of a flamenco dancer"></div>
  <p class="caps giftcard">Giftcard</p>
</section>

<section class="panel carrier-inside" aria-label="Gift card carrier, inside">
  <div class="paisley-fill" role="img" aria-label="Soft grey paisley pattern"></div>
  <div class="field to">To:<span class="line"></span></div>
  <div class="field from">From:<span class="line"></span></div>
  <div class="field amount">Amount:<span class="line"></span></div>
</section>

<section class="panel card-front" aria-label="Gift card front">
  <div class="dancer" role="img" aria-label="Red line drawing of a flamenco dancer"></div>
  <p class="caps url">www.corvo-la-mesa.com</p>
</section>

<section class="panel card-back" aria-label="Gift card back">
  <div class="paisley-fill" role="img" aria-label="Soft grey paisley pattern"></div>
  <p class="terms">
    Additional value may be added to this card at any time.<br>
    We are not reponsible for lost, stolen, or damaged cards or any unauthorized card use.<br>
    Cards that are lost, stolen, or damaged cannot be replaced and have no value.<br>
    Cards cannot be redeemed for cash and cannot be used toward tax and tips.<br>
    Card expires 180 calendar days after issue date.
  </p>
  <p class="back-address">Valdoreno Tapas Bar<br>2817 West Pellham Street<br>Chicago, IL 60641</p>
  <div class="holo" role="img" aria-label="Security hologram patch"></div>
  <div class="sig-strip"></div>
</section>

</body>
</html>
```